Eco-friendly waste company needs flyer design to promote collections

We need a flyer to promote our new small item collection service, offering cheaper waste collections to customers who usually would not want to pay for our high-eco performance business (we are expensive compared to companies who dispose of their waste in less eco-friendly ways). This flyer needs to be professional, informational, and classy to appeal to corporate office-based customers. We want photos used where possible, not cartoon or illustrations of objects we collect. I will attach our logo in various designs, and am really open to design options. We have a website that is ourdated, uses cartoons etc, and this is not landing well with our customer base so we want to move away from that kind of design. I need an A5-sized flyer, double sided. Please ask me if you have any questions!
Hi all,
Thank you all so much for so many wonderful designs, I will be looking through all of these tomorrow with my CEO and then I will update the project status again.
Thanks!!
Kind regards,
Lena

Hi all,
Thanks!!
Kind regards,
Lena

```html
<!DOCTYPE html>
<html lang="en">
<head>
<meta charset="utf-8">
<title>Fernleigh – Small Item Collection Flyer</title>
<link rel="stylesheet" href="https://fonts.googleapis.com/css2?family=Montserrat:wght@400;500;600;700&display=swap">
<style>
  :root{
    --green:#2fa987;
    --dark:#353a31;
    --ink:#2a2a2a;
    --paper:#ffffff;
    --backdrop:#eceeed;
  }
  *{box-sizing:border-box;margin:0;padding:0}
  html,body{width:900px;height:1200px;overflow:hidden}
  body{background:var(--backdrop);font-family:'Montserrat',Arial,sans-serif;color:var(--ink);position:relative}
  .flyer{position:absolute;top:303px;width:420px;height:594px;background:var(--paper);overflow:hidden;box-shadow:0 4px 14px rgba(0,0,0,.18)}
  .flyer--front{left:20px}
  .flyer--back{left:460px}
  .hero{position:absolute;left:0;top:0;width:420px;height:197px}
  .hero--van{background:linear-gradient(160deg,#7f97b0 0%,#aab3b8 35%,#d7d9d6 55%,#5d625f 80%,#2f3331 100%)}
  .hero--scrap{background:linear-gradient(200deg,#f2a24a 0%,#b8784a 22%,#6f6458 50%,#46504f 75%,#313736 100%)}
  .hero-curve{position:absolute;left:0;top:0;width:420px;height:240px}
  .brand{position:absolute;left:63px;top:141px;width:110px;height:110px;border-radius:50%;background:var(--paper);border:3px solid var(--green);display:flex;align-items:center;justify-content:center;text-align:center}
  .brand-name{font-weight:600;font-size:16px;color:var(--dark);letter-spacing:.2px}
  .url-band{position:absolute;left:173px;top:200px;width:247px;height:26px;background:var(--green);color:#fff;font-weight:700;font-size:11.6px;display:flex;align-items:center;padding-left:9px;letter-spacing:.1px}
  .side-panel{position:absolute;left:240px;top:226px;width:180px;height:290px;background:var(--dark);border-bottom-left-radius:40px;color:#fff;padding:0 14px 0 18px}
  .side-title{font-weight:600;font-size:10px;line-height:1.2}
  .bullets{list-style:none;font-size:8.6px;line-height:1.22}
  .bullets li{padding-left:10px;position:relative;margin-bottom:5.2px}
  .bullets li::before{content:"•";position:absolute;left:3px}
  .side-panel .bullets li{margin-bottom:5.6px}
  .center-col{position:absolute;left:8px;width:220px;text-align:center}
  .headline{font-weight:700;font-size:12.6px;line-height:1.12}
  .accent{color:var(--green);font-weight:500;font-size:9.6px;line-height:1.25}
  .price{font-weight:700;font-size:12.6px}
  .challenge{position:absolute;left:11px;top:430px;width:219px;height:84px;border:1.5px dashed var(--green);padding:7px 10px;font-size:8.6px;line-height:1.25}
  .challenge p+p{margin-top:8px}
  .challenge .email{color:var(--green)}
  .challenge .phone{font-weight:700;font-size:10.4px}
  .conditions{position:absolute;left:21px;top:535px;font-size:8.4px;line-height:1.55;width:390px}
  .conditions h3{font-size:9.4px;font-weight:600}
  .conditions .label{color:var(--green)}
  .footer-line{position:absolute;left:0;top:582px;width:420px;height:2px;background:var(--green)}
  .footer-bar{position:absolute;left:0;top:586px;width:420px;height:8px;background:var(--dark)}
  .left-col{position:absolute;left:21px;width:205px}
  .left-col .headline{font-size:10.2px;font-weight:700;line-height:1.15}
  .left-col .accent{margin:10px 0 4px;font-size:8.8px}
  .left-col .bullets{color:var(--ink)}
  .closing{position:absolute;left:14px;width:392px;text-align:center;font-size:8.6px;line-height:1.25}
  .closing .accent{font-size:8.6px;margin-top:8px}
</style>
</head>
<body>

<section class="flyer flyer--front">
  <div class="hero hero--van" role="img" aria-label="Photo of two crew members loading a white branded collection truck outside a warehouse"></div>
  <svg class="hero-curve" viewBox="0 0 420 240" aria-hidden="true">
    <path d="M0 95 C15 160 60 195 130 205 L130 240 L0 240 Z" fill="#fff"/>
    <path d="M0 95 C15 160 60 195 130 205 L130 212 C60 210 18 175 0 125 Z" fill="#2fa987"/>
  </svg>
  <div class="brand"><span class="brand-name">Fernleigh</span></div>
  <div class="url-band">www.fernleighrecycling.com</div>

  <aside class="side-panel">
    <h3 class="side-title" style="margin:10px 0 10px">Example items are:</h3>
    <ul class="bullets">
      <li>Printers</li>
      <li>Office furniture</li>
      <li>Whiteboards</li>
      <li>Shredders</li>
      <li>PC or television monitors</li>
      <li>Fans</li>
      <li>Plants and planter boxes</li>
      <li>Books and magazines<br>(max 25kg)</li>
      <li>Pallet</li>
      <li>Packaging (cardboard boxes, polystyrene, plastic etc.)</li>
      <li>Paints and chemicals<br>(max 7 litres)</li>
      <li>Light bulbs and fluorescent tubes (max 10 pieces)</li>
    </ul>
  </aside>

  <div class="center-col" style="top:284px">
    <h1 class="headline">Do you have small or single items that cost too much to dispose of?</h1>
    <p class="accent" style="margin-top:14px">Are you located in Central London?<br>Fernleigh has the solution for you.</p>
    <p class="accent" style="margin-top:14px">We can collect items for <span class="price" style="color:var(--ink)">£25</span> each<br>on Wednesdays.</p>
  </div>

  <div class="challenge">
    <p>We can take most things you can’t put in your normal bins – <strong>challenge us!</strong></p>
    <p>If you have any questions please email us at <span class="email">bookings@fernleighrecycling.com</span> or call us on <span class="phone">020 4000 5821</span>.</p>
  </div>

  <div class="conditions">
    <h3>Conditions of offer:</h3>
    <p>Price is exclusive of VAT.</p>
    <p><span class="label">Eligible postcodes:</span> EC1, EC2, EC3, EC4, WC1, WC2, W1, SW1, SE1, E1, E2, N1, NW1</p>
  </div>

  <div class="footer-line"></div>
  <div class="footer-bar"></div>
</section>

<section class="flyer flyer--back">
  <div class="hero hero--scrap" role="img" aria-label="Photo of a worker in a hard hat and hi-vis vest sorting scrap at a recycling yard in warm sunlight"></div>
  <svg class="hero-curve" viewBox="0 0 420 240" aria-hidden="true">
    <path d="M0 95 C15 160 60 195 130 205 L130 240 L0 240 Z" fill="#fff"/>
    <path d="M0 95 C15 160 60 195 130 205 L130 212 C60 210 18 175 0 125 Z" fill="#2fa987"/>
  </svg>
  <div class="brand"><span class="brand-name">Fernleigh</span></div>
  <div class="url-band">www.fernleighrecycling.com</div>

  <aside class="side-panel" style="padding-right:22px">
    <h3 class="side-title" style="margin:30px 0 12px">Need to securely destroy data on your computer or server?</h3>
    <p style="font-size:8.6px;line-height:1.22;margin-bottom:6px">Need to securely destroy data on your computer or server?</p>
    <ul class="bullets">
      <li>Computers</li>
      <li>Laptops</li>
      <li>Servers</li>
      <li>Routers</li>
      <li>Switches</li>
      <li>Mobile phones</li>
      <li>Landline phones</li>
      <li>Printers with memory</li>
      <li>Photocopiers with memory</li>
    </ul>
  </aside>

  <div class="left-col" style="top:289px">
    <h2 class="headline">Need to get rid of items which can’t go in your normal bin?</h2>
    <p class="accent">We collect the following hazardous items:</p>
    <ul class="bullets">
      <li>Paint - £4 per litre</li>
      <li>Fluorescent tubes and bulbs - £4 each</li>
      <li>Cooking oil / hydraulic oil / hazardous liquids – from £5 per litre</li>
      <li>TV / Computer monitors - £10 each</li>
      <li>Batteries – from £5 per kilo<br>(depends on type)</li>
      <li>Gas bottles &amp; fire extinguishers - £35 each Fridges – £40 for a small fridge, £125 for a commercial fridge, £200 for an ammonia fridge each</li>
      <li>Air conditioners - £30 each</li>
    </ul>
  </div>

  <div class="closing" style="top:528px">
    <p>We can provide certificates confirming data secure destruction, either through securing wiping and reuse, or through shredding and recycling.</p>
    <p class="accent">We can also securely destroy any paper, files, documents etc with our shredding service.</p>
  </div>

  <div class="footer-line"></div>
  <div class="footer-bar"></div>
</section>

</body>
</html>
```